Coach Remy Talbek Life Coach webpage

I am a Triathlon Coach but now I am in the process of opening a "new brand" as a Life Coach therefore I need new image and a new webpage. I live in Mexico city and would like to offer my services to Latinamerican clientes (spanish speaking). My actual website is www.quorvane.mx. My new website should help me to communicate what I do (Life Coaching), how my services are different from others, help gain new clients through one on one sessions, and I also offer a mental training course. I would like to see designs from a ZEN perspective (minimalistic, light and peaceful colors and not strong colors like my current webpage). The final design should communicate a sense of peace, tranquility, accomplishment and accompaniment. I would like to be able to manipulate the information and add-ons such a section were people can buy, subscribe and pay for the courses.

Target Market(s)

Male and female between 35 and 60 years who are going through changes in their life, need to make important decisions (such a divorcing or not, quitting or changing jobs, or not, etc), and or who do not fell happy with their current life.

Industry/Entity Type

Coaching

Coding

Number of Pages Required

5+ page

Font styles to use
Sans Serif

Colors

Designer to choose colors to be used in the design.

Requirements
Must have
• 6 sections and one of those sections a place where my clients can buy courses and pay for them there. I would like to be able to change some of the information easily. I would like to see designs from a ZEN perspective (minimalistic, light and peaceful colors and not strong colors like my current webpage). The final design should communicate a sense of peace, tranquility, accomplishment and accompaniment. I would like to be able to manipulate the informati
Should not have
• dark strong colors

```html
<!DOCTYPE html>
<html lang="en">
<head>
<meta charset="UTF-8">
<title>Remy Talbek — Life Coach</title>
<link href="https://fonts.googleapis.com/css2?family=Cinzel:wght@600;700&family=Outfit:wght@400;500;600&display=swap" rel="stylesheet">
<style>
:root{
  --sage:#6f8b81;
  --sage-light:#8fa69c;
  --forest:#4a5f58;
  --forest-deep:#3e514b;
  --lime:#abb72b;
  --mint:#e8f2ee;
  --mint-row:#dcebe5;
  --ink:#1e3a39;
  --body:#2b2b2b;
  --white:#ffffff;
}
*{margin:0;padding:0;box-sizing:border-box}
html,body{width:1200px;height:4368px;overflow:hidden}
body{font-family:'Outfit',sans-serif;color:var(--body);background:var(--white);position:relative}
section,header,footer{position:absolute;left:0;width:1200px}
.abs{position:absolute}
.heading{font-family:'Cinzel',serif;font-weight:700;color:var(--ink);letter-spacing:1px}
.btn{display:inline-block;background:var(--lime);color:var(--white);font-size:14px;font-weight:500;padding:10px 20px;border-radius:3px}
.btn-outline{display:inline-block;border:1px solid var(--ink);color:var(--ink);font-size:13px;padding:8px 16px;border-radius:3px}
.para{font-size:15px;line-height:1.55}

/* Hero */
.hero{top:0;height:600px;background:linear-gradient(180deg,#6c887e 0%,#8ea59b 55%,#7d978c 100%)}
.logo{font-family:'Cinzel',serif;font-weight:700;color:var(--white);font-size:24px;letter-spacing:1px}
.nav{top:30px;left:540px;display:flex;gap:30px;font-size:14px;color:var(--white)}
.nav .active{border-bottom:2px solid var(--white);padding-bottom:3px}
.hero-kicker{left:144px;top:158px;color:var(--white);font-size:15px;font-weight:600;letter-spacing:1px}
.hero-title{left:144px;top:186px;color:var(--white);font-size:50px}
.hero-list{left:144px;top:250px;list-style:none;color:var(--white);font-size:15px}
.hero-list li{display:flex;align-items:center;gap:12px;height:26px}
.hero-list li::before{content:"";width:10px;height:10px;border-radius:50%;background:var(--white)}
.hero-photo{left:612px;top:100px;width:448px;height:500px;border-radius:40px 60px 0 60px;background:linear-gradient(180deg,#e5a46a 0%,#c46a34 45%,#5a3b2c 100%)}
.arrow{width:28px;height:28px;border-radius:50%;background:var(--white);display:flex;align-items:center;justify-content:center}

/* About */
.about{top:600px;height:600px;background:var(--white)}
.about-photo{left:144px;top:100px;width:436px;height:440px;border-radius:0 60px 0 60px;background:linear-gradient(160deg,#e9e6e1,#bdb6ad)}
.about-accent{left:120px;top:420px;width:100px;height:100px;border-radius:50%;background:var(--lime)}

/* Services */
.services{top:1200px;height:700px;background:var(--mint)}
.card{background:var(--white);padding:24px 32px}
.card-icon{width:110px;height:110px;border-radius:50%;background:var(--lime)}
.card-title{font-size:24px;font-weight:600;color:var(--ink);line-height:1.25}

/* Blog */
.blog{top:1900px;height:640px;background:var(--white)}
.post-photo{height:192px;background:linear-gradient(150deg,#d9cfc4,#9a8b7e)}
.post-date{font-size:14px;display:flex;gap:8px;align-items:center;margin-top:26px}
.post-title{font-size:17px;font-weight:600;margin:6px 0 6px}

/* Contact */
.contact{top:2540px;height:760px;background:linear-gradient(180deg,#6b877d,#5d786e)}
.contact-photo{left:144px;top:172px;width:436px;height:468px;border-radius:0 40px 0 0;background:linear-gradient(160deg,#b9ae9d,#6f6a5d)}
.field{left:600px;width:460px;height:50px;border:1.5px solid var(--white);border-radius:25px;color:var(--white);font-size:14px;padding:15px 22px}

/* FAQ */
.faq{top:3300px;height:660px;background:var(--white)}
.faq-row{left:256px;width:688px;height:56px;background:var(--mint-row);display:flex;align-items:center;justify-content:space-between;padding:0 20px;font-size:17px;font-weight:500;color:var(--ink)}
.faq-plus{width:34px;height:34px;border-radius:50%;background:var(--lime);color:var(--white);display:flex;align-items:center;justify-content:center;font-size:22px}

/* Footer */
.footer{top:3960px;height:408px;background:var(--forest)}
.foot-head{font-size:18px;font-weight:600;color:var(--white);letter-spacing:.5px}
.foot-text{font-size:14px;color:var(--white);line-height:1.6}
.social{width:36px;height:36px;border-radius:50%;background:var(--white)}
.links{list-style:none;font-size:14px;color:var(--white)}
.links li{height:28px;display:flex;align-items:center;gap:10px}
.links li::before{content:"›";font-size:16px}
.footer-bar{left:0;top:356px;width:1200px;height:52px;background:var(--forest-deep);color:var(--white);font-size:14px;display:flex;align-items:center;justify-content:center}
</style>
</head>
<body>

<header class="hero">
  <div class="abs logo" style="left:144px;top:22px">REMY TALBEK</div>
  <nav class="abs nav"><span class="active">Home</span><span>About</span><span>Services</span><span>Blog</span><span>Contact</span></nav>
  <span class="abs btn" style="left:936px;top:22px">Get A Quote</span>

  <div class="abs hero-kicker">WELCOME TO</div>
  <h1 class="abs heading hero-title" style="color:var(--white)">REMY TALBEK</h1>
  <ul class="abs hero-list">
    <li>Lorem ipsum dolor sit amet, consectetur adipiscing</li>
    <li>Lorem ipsum dolor sit amet, consectetur adipiscing</li>
    <li>Lorem ipsum dolor sit amet, consectetur adipiscing</li>
  </ul>
  <span class="abs btn" style="left:144px;top:384px">Schedule a Free Consultation</span>
  <div class="abs" style="left:144px;top:478px;display:flex;gap:10px">
    <span class="arrow"><svg width="12" height="12" viewBox="0 0 12 12"><path d="M8 1 3 6l5 5" fill="none" stroke="#1e3a39" stroke-width="2"/></svg></span>
    <span class="arrow"><svg width="12" height="12" viewBox="0 0 12 12"><path d="M4 1l5 5-5 5" fill="none" stroke="#1e3a39" stroke-width="2"/></svg></span>
  </div>
  <div class="abs hero-photo" role="img" aria-label="Person raising joined hands toward a sunset over mountains"></div>
</header>

<section class="about">
  <div class="abs about-accent"></div>
  <div class="abs about-photo" role="img" aria-label="Smiling coach seated at a desk"></div>
  <h2 class="abs heading" style="left:612px;top:96px;font-size:46px">ABOUT ME</h2>
  <p class="abs para" style="left:612px;top:160px;width:450px">Lorem ipsum dolor sit amet, consectetur adipiscing elit, sed do eiusmod tempor incididunt ut labore et dolore magna aliqua. Ut enim ad minim veniam, quis nostrud exercitation ullamco laboris nisi ut aliquip ex ea commodo consequat. Duis aute irure dolor in reprehenderit in voluptate velit esse cillum dolore eu fugiat nulla pariatur. Excepteur sint occaecat cupidatat non proident, sunt in culpa qui officia deserunt mollit anim id est laborum. Lorem ipsum dolor sit amet, consectetur adipiscing elit, sed do eiusmod tempor incididunt ut labore et dolore magna aliqua. Ut enim ad minim veniam, quis nostrud exercitation ullamco laboris nisi ut aliquip ex ea commodo consequat. Duis aute irure dolor in reprehenderit in voluptate velit esse cillum dolore eu fugiat nulla pariatur.</p>
  <span class="abs btn" style="left:612px;top:458px">Learn More</span>
</section>

<section class="services">
  <h2 class="abs heading" style="left:0;width:1200px;text-align:center;top:88px;font-size:46px">OUR SERVICES</h2>
  <div class="abs card" style="left:144px;top:168px;width:444px;height:424px">
    <div style="display:flex;gap:24px;align-items:center">
      <div class="card-icon" role="img" aria-label="Life coaching icon"></div>
      <div class="card-title">Personalized<br>Life Coaching</div>
    </div>
    <p class="para" style="margin:20px 0 18px">Lorem ipsum dolor sit amet, consectetur adipiscing elit, sed do eiusmod tempor incididunt ut labore et dolore magna aliqua. Ut enim ad minim veniam, quis nostrud exercitation ullamco laboris nisi ut aliquip ex ea commodo consequat. Duis aute irure dolor in reprehenderit in voluptate velit esse cillum dolore eu fugiat nulla pariatur.</p>
    <span class="btn-outline">Learn More</span>
  </div>
  <div class="abs card" style="left:612px;top:168px;width:448px;height:424px">
    <div style="display:flex;gap:24px;align-items:center">
      <div class="card-icon" role="img" aria-label="Mental training icon"></div>
      <div class="card-title">Mental Training<br>Courses</div>
    </div>
    <p class="para" style="margin:20px 0 18px">Lorem ipsum dolor sit amet, consectetur adipiscing elit, sed do eiusmod tempor incididunt ut labore et dolore magna aliqua. Ut enim ad minim veniam, quis nostrud exercitation ullamco laboris nisi ut aliquip ex ea commodo consequat. Duis aute irure dolor in reprehenderit in voluptate velit esse cillum dolore eu fugiat nulla pariatur.</p>
    <span class="btn-outline">Learn More</span>
  </div>
</section>

<section class="blog">
  <h2 class="abs heading" style="left:0;width:1200px;text-align:center;top:92px;font-size:46px">LATEST BLOG</h2>
  <article class="abs" style="left:144px;top:180px;width:284px">
    <div class="post-photo" role="img" aria-label="Two women talking in a bright room"></div>
    <div class="post-date"><svg width="14" height="14" viewBox="0 0 14 14"><rect x="1" y="2" width="12" height="11" rx="1" fill="none" stroke="#1e3a39" stroke-width="1.5"/><path d="M1 5.5h12" stroke="#1e3a39" stroke-width="1.5"/></svg>Jan 20, 2024</div>
    <h3 class="post-title">Lorem ipsum dolor sit amet</h3>
    <p class="para">Lorem ipsum dolor sit amet, consectetur adipiscing elit, sed do eiusmod tempor incididunt ut labore et dolore magna aliqua.</p>
  </article>
  <article class="abs" style="left:460px;top:180px;width:284px">
    <div class="post-photo" role="img" aria-label="Small group in a coaching session"></div>
    <div class="post-date"><svg width="14" height="14" viewBox="0 0 14 14"><rect x="1" y="2" width="12" height="11" rx="1" fill="none" stroke="#1e3a39" stroke-width="1.5"/><path d="M1 5.5h12" stroke="#1e3a39" stroke-width="1.5"/></svg>Jan 20, 2024</div>
    <h3 class="post-title">Lorem ipsum dolor sit amet</h3>
    <p class="para">Lorem ipsum dolor sit amet, consectetur adipiscing elit, sed do eiusmod tempor incididunt ut labore et dolore magna aliqua.</p>
  </article>
  <article class="abs" style="left:772px;top:180px;width:288px">
    <div class="post-photo" role="img" aria-label="Woman holding a tablet in an office"></div>
    <div class="post-date"><svg width="14" height="14" viewBox="0 0 14 14"><rect x="1" y="2" width="12" height="11" rx="1" fill="none" stroke="#1e3a39" stroke-width="1.5"/><path d="M1 5.5h12" stroke="#1e3a39" stroke-width="1.5"/></svg>Jan 20, 2024</div>
    <h3 class="post-title">Lorem ipsum dolor sit amet</h3>
    <p class="para">Lorem ipsum dolor sit amet, consectetur adipiscing elit, sed do eiusmod tempor incididunt ut labore et dolore magna aliqua.</p>
  </article>
</section>

<section class="contact">
  <h2 class="abs heading" style="left:0;width:1200px;text-align:center;top:86px;font-size:46px;color:var(--white)">CONTACT US</h2>
  <div class="abs contact-photo" role="img" aria-label="Woman relaxing on a sofa with a phone"></div>
  <div class="abs field" style="top:180px">Your name</div>
  <div class="abs field" style="top:252px">Email</div>
  <div class="abs field" style="top:324px">Phone</div>
  <div class="abs field" style="top:396px;height:180px;border-radius:22px">Message</div>
  <span class="abs btn" style="left:600px;top:604px">Submit Now</span>
</section>

<section class="faq">
  <h2 class="abs heading" style="left:0;width:1200px;text-align:center;top:90px;font-size:36px">FREQUENTLY ASKED QUESTIONS</h2>
  <div class="abs faq-row" style="top:144px">Lorem ipsum dolor sit amet, consectetur adipiscing elit<span class="faq-plus">+</span></div>
  <div class="abs faq-row" style="top:236px">Lorem ipsum dolor sit amet, consectetur adipiscing elit<span class="faq-plus">+</span></div>
  <div class="abs faq-row" style="top:328px">Lorem ipsum dolor sit amet, consectetur adipiscing elit<span class="faq-plus">+</span></div>
  <div class="abs faq-row" style="top:420px">Lorem ipsum dolor sit amet, consectetur adipiscing elit<span class="faq-plus">+</span></div>
  <div class="abs faq-row" style="top:512px">Lorem ipsum dolor sit amet, consectetur adipiscing elit<span class="faq-plus">+</span></div>
  <span class="abs btn" style="left:528px;top:600px">View More FAQ</span>
</section>

<footer class="footer">
  <div class="abs logo" style="left:144px;top:104px">REMY TALBEK</div>
  <div class="abs" style="left:156px;top:166px;display:flex;gap:14px">
    <span class="social"></span><span class="social"></span><span class="social"></span>
  </div>

  <div class="abs foot-head" style="left:460px;top:100px">CONTACT INFO</div>
  <div class="abs" style="left:460px;top:140px;display:flex;flex-direction:column;gap:14px">
    <div style="display:flex;gap:14px"><svg width="16" height="20" viewBox="0 0 16 20"><path d="M8 1a6 6 0 0 0-6 6c0 5 6 12 6 12s6-7 6-12a6 6 0 0 0-6-6z" fill="#fff"/><circle cx="8" cy="7" r="2.2" fill="#4a5f58"/></svg><div class="foot-text"><b>Address :</b><br>123, Lorem ipsum dolor sit</div></div>
    <div style="display:flex;gap:14px"><svg width="16" height="14" viewBox="0 0 16 14"><rect x="0.5" y="1" width="15" height="12" rx="1" fill="#fff"/><path d="M1 2l7 5 7-5" fill="none" stroke="#4a5f58" stroke-width="1.3"/></svg><div class="foot-text"><b>Email</b><br>hola@quorvane.mx</div></div>
    <div style="display:flex;gap:14px"><svg width="16" height="16" viewBox="0 0 16 16"><path d="M3 1l3 3-2 2c1 2 3 4 5 5l2-2 3 3-2 3C7 15 1 9 1 3z" fill="#fff"/></svg><div class="foot-text"><b>Phone</b><br>+52 55 0100 2030</div></div>
  </div>

  <div class="abs foot-head" style="left:748px;top:100px">QUICK LINKS</div>
  <ul class="abs links" style="left:748px;top:140px"><li>Home</li><li>About</li><li>Services</li><li>Contact</li></ul>
  <ul class="abs links" style="left:900px;top:140px"><li>Terms and Condition</li><li>Privacy policy</li><li>Help</li><li>Support</li></ul>

  <div class="abs footer-bar">© Copyrights 2024 | All Rights Reserved</div>
</footer>

</body>
</html>
```